Magnetic Business card Design do a service provider

Hi,

The company aim is to provide all service needs under one roof. However, at the moment there is only Accounting, Electrical and IT branches. There will be more services coming onboard in the future.

I already have a logo designed (Company name is already part of the logo), I now need a magnetic business card designed.

The business card will contain the following:

- Company Logo
- Contact#
- E-mail
- enough space to add website URL (for future)
Updates

Project Deadline Extended Reason: HI All,The deadline has been extended due to not having enough time to review an overwhelming number of designs that has been submitted by lots of designers.I will be uploading a draft of designs that i have in mind.Thanks. Added Friday, January 22, 2016

Target Market(s)

Residential, Home-based Businesses, Small and Medium businesses

Industry/Entity Type

Business

Contact Information for Business Card

Contact#: 0491 738 520
E-mail: service@brightlanetrades.net.au

Font styles to use
Decorative
Script

Requirements
Must have
• Round edges
• Some form of logo incorporation as a background

```html
<!DOCTYPE html>
<html lang="en">
<head>
<meta charset="utf-8">
<title>Bright Lane Trades – Business Card</title>
<link href="https://fonts.googleapis.com/css2?family=Dancing+Script:wght@500&display=swap" rel="stylesheet">
<style>
  :root {
    --backdrop: #2b2b2b;
    --card: #ffffff;
    --navy: #1d3f8f;
    --sky: #2a9fd8;
    --card-shadow: rgba(0, 0, 0, 0.45);
  }
  html, body {
    margin: 0;
    padding: 0;
    width: 1200px;
    height: 913px;
    overflow: hidden;
    background: var(--backdrop);
  }
  .stage {
    width: 1200px;
    height: 913px;
    display: flex;
    align-items: center;
    justify-content: center;
  }
  .business-card {
    position: relative;
    width: 800px;
    height: 490px;
    background: var(--card);
    border-radius: 36px;
    box-shadow: 0 18px 40px var(--card-shadow);
    box-sizing: border-box;
  }
  .brand {
    position: absolute;
    left: 80px;
    top: 248px;
    display: flex;
    align-items: center;
    gap: 14px;
  }
  .brand-dot {
    width: 22px;
    height: 22px;
    border-radius: 50%;
    background: var(--navy);
    flex: none;
  }
  .brand-name {
    font-family: "Dancing Script", cursive;
    font-weight: 500;
    font-size: 44px;
    line-height: 1;
    color: var(--navy);
    white-space: nowrap;
  }
  .divider {
    position: absolute;
    left: 440px;
    top: 210px;
    width: 2px;
    height: 100px;
    background: var(--sky);
  }
  .contact {
    position: absolute;
    left: 470px;
    top: 214px;
    font-family: "Dancing Script", cursive;
    font-weight: 500;
    color: var(--navy);
  }
  .contact-phone {
    margin: 0;
    font-size: 40px;
    line-height: 1.1;
  }
  .contact-email {
    margin: 6px 0 0;
    font-size: 19px;
    line-height: 1.2;
    white-space: nowrap;
  }
</style>
</head>
<body>
  <main class="stage">
    <article class="business-card">
      <div class="brand">
        <span class="brand-dot" aria-hidden="true"></span>
        <span class="brand-name">Bright Lane Trades</span>
      </div>
      <div class="divider" aria-hidden="true"></div>
      <address class="contact">
        <p class="contact-phone">0491 738 520</p>
        <p class="contact-email">service@brightlanetrades.net.au</p>
      </address>
    </article>
  </main>
</body>
</html>
```